Dental Medical History Form - Content provided

Design a medical history form for a dental practice. Content is provided so all that is needed is the formatting to make it look great and easy to read.

"Patient Information" to include all information contained in top portion of the "Patient Medical History Form" docx file.

"Medical History" should follow the formatting and content of the "Exact Medical History" file as this is what the entry fields look like in our practice software and so we would like it to match.

1st page - Patient info, allergies, medications, antibiotics, joint replacement, pregnancy.

2nd page - Do you have, or have you had, any of the following? . . . . . . .
Updates

Project Deadline Extended Reason: Picked too short of a deadline to start (2 days) Added Monday, February 13, 2017

Target Market(s)

All ages but must be clear enough for elderly to read. Use as much space as possible to keep font size bigger yet keep to two pages

Industry/Entity Type

Dental

Font styles to use
Sans Serif

Requirements
Must have
• All content provided
• Our logo at the top (file provided)
• Century Gothic Font
• Limit to two pages

```html
<!DOCTYPE html>
<html lang="en">
<head>
<meta charset="utf-8">
<title>Dental Medical History Form – Page 2</title>
<link href="https://fonts.googleapis.com/css2?family=Asap+Condensed:ital,wght@0,400;0,600;0,700;1,400;1,600;1,700&display=swap" rel="stylesheet">
<style>
  :root{
    --backdrop:#6ccbe8;
    --paper:#ffffff;
    --paper-tint:#eef5fc;
    --ink:#1f3a78;
    --ink-strong:#142c66;
    --accent:#1b6fa8;
    --band-dark:#1d3f8f;
    --band-light:#2f9fd3;
    --box:#7fb6dc;
    --rule:#1b6fa8;
  }
  *{box-sizing:border-box;margin:0;padding:0}
  html,body{width:1200px;height:784px;overflow:hidden}
  body{
    background:var(--backdrop);
    font-family:"Asap Condensed",sans-serif;
    color:var(--ink);
    position:relative;
  }
  .form-page{
    position:absolute;left:337px;top:20px;width:526px;height:744px;
    background:linear-gradient(180deg,var(--paper) 0%,var(--paper) 70%,var(--paper-tint) 100%);
    box-shadow:0 6px 18px rgba(20,60,110,.25);
    overflow:hidden;
  }
  .question-band{
    height:34px;
    background:linear-gradient(180deg,var(--band-light),var(--accent));
    color:#fff;font-style:italic;font-weight:700;font-size:14px;
    display:flex;align-items:center;justify-content:center;
    letter-spacing:.2px;
  }
  .history-columns{
    display:flex;gap:18px;padding:14px 22px 0 26px;
  }
  .history-col{flex:1}
  .section-title{
    font-weight:700;font-style:italic;font-size:11.5px;color:var(--ink-strong);
    height:15px;line-height:15px;
  }
  .item{
    display:flex;align-items:center;height:15px;
    font-style:italic;font-size:10.5px;
  }
  .item-name{flex:1;white-space:nowrap;overflow:hidden}
  .answer{display:flex;align-items:center;gap:3px;width:40px;font-size:9.5px}
  .tick-box{width:9px;height:9px;border:1px solid var(--box);background:#fff}
  .sign-off{
    position:absolute;left:26px;right:22px;bottom:38px;
  }
  .sign-lines{display:flex;gap:40px;margin-bottom:10px}
  .sign-field{display:flex;align-items:flex-end;gap:8px;flex:1}
  .sign-label{font-weight:700;font-style:italic;font-size:12px;color:var(--accent)}
  .sign-rule{flex:1;border-bottom:1px solid var(--rule);height:14px}
  .sign-field.date{flex:0 0 150px}
  .thanks{font-style:italic;font-size:9px;color:var(--accent);line-height:1.35}
  .footer-band{
    position:absolute;left:0;right:0;bottom:0;height:10px;
    background:linear-gradient(90deg,var(--band-dark),var(--band-light));
  }
  .footer-tab{
    position:absolute;left:150px;bottom:10px;width:100px;height:8px;
    background:var(--band-light);border-radius:4px 4px 0 0;
  }
</style>
</head>
<body>
<main class="form-page">
  <header class="question-band">Do you have, or have you had, any of the following?</header>

  <section class="history-columns">
    <div class="history-col">
      <div class="section-title">Dental</div>
      <div class="item"><span class="item-name">Acid Reflux</span><span class="answer">Yes<i class="tick-box"></i></span><span class="answer">No<i class="tick-box"></i></span></div>
      <div class="item"><span class="item-name">Bad Breath/Taste</span><span class="answer">Yes<i class="tick-box"></i></span><span class="answer">No<i class="tick-box"></i></span></div>
      <div class="item"><span class="item-name">Bleeding/Swollen/Sore Gums</span><span class="answer">Yes<i class="tick-box"></i></span><span class="answer">No<i class="tick-box"></i></span></div>
      <div class="item"><span class="item-name">Blisters/Ulcers in Mouth</span><span class="answer">Yes<i class="tick-box"></i></span><span class="answer">No<i class="tick-box"></i></span></div>
      <div class="item"><span class="item-name">Broken tooth/filling</span><span class="answer">Yes<i class="tick-box"></i></span><span class="answer">No<i class="tick-box"></i></span></div>
      <div class="item"><span class="item-name">Burning tongue</span><span class="answer">Yes<i class="tick-box"></i></span><span class="answer">No<i class="tick-box"></i></span></div>
      <div class="item"><span class="item-name">Dry mouth</span><span class="answer">Yes<i class="tick-box"></i></span><span class="answer">No<i class="tick-box"></i></span></div>
      <div class="item"><span class="item-name">Food collection between teeth</span><span class="answer">Yes<i class="tick-box"></i></span><span class="answer">No<i class="tick-box"></i></span></div>
      <div class="item"><span class="item-name">Grinding/clenching teeth (day/night)</span><span class="answer">Yes<i class="tick-box"></i></span><span class="answer">No<i class="tick-box"></i></span></div>
      <div class="item"><span class="item-name">Loose teeth</span><span class="answer">Yes<i class="tick-box"></i></span><span class="answer">No<i class="tick-box"></i></span></div>
      <div class="item"><span class="item-name">Crooked teeth</span><span class="answer">Yes<i class="tick-box"></i></span><span class="answer">No<i class="tick-box"></i></span></div>
      <div class="item"><span class="item-name">Discoloured teeth</span><span class="answer">Yes<i class="tick-box"></i></span><span class="answer">No<i class="tick-box"></i></span></div>
      <div class="item"><span class="item-name">Sensitivity to Hot/Cold</span><span class="answer">Yes<i class="tick-box"></i></span><span class="answer">No<i class="tick-box"></i></span></div>
      <div class="item"><span class="item-name">Tooth pain when chewing</span><span class="answer">Yes<i class="tick-box"></i></span><span class="answer">No<i class="tick-box"></i></span></div>
      <div class="item"><span class="item-name">Jaw pain/Fracture</span><span class="answer">Yes<i class="tick-box"></i></span><span class="answer">No<i class="tick-box"></i></span></div>
      <div class="item"><span class="item-name">Orthodontic treatment/history</span><span class="answer">Yes<i class="tick-box"></i></span><span class="answer">No<i class="tick-box"></i></span></div>
      <div class="item"><span class="item-name">Oral Cancer</span><span class="answer">Yes<i class="tick-box"></i></span><span class="answer">No<i class="tick-box"></i></span></div>
      <div class="section-title">Diet/Lifestyle</div>
      <div class="item"><span class="item-name">Drink more than one glass alcohol per day</span><span class="answer">Yes<i class="tick-box"></i></span><span class="answer">No<i class="tick-box"></i></span></div>
      <div class="item"><span class="item-name">Smoking</span><span class="answer">Yes<i class="tick-box"></i></span><span class="answer">No<i class="tick-box"></i></span></div>
      <div class="item"><span class="item-name">Carbonated drinks</span><span class="answer">Yes<i class="tick-box"></i></span><span class="answer">No<i class="tick-box"></i></span></div>
      <div class="item"><span class="item-name">Sugary foods</span><span class="answer">Yes<i class="tick-box"></i></span><span class="answer">No<i class="tick-box"></i></span></div>
      <div class="section-title">Blood</div>
      <div class="item"><span class="item-name">Anaemia</span><span class="answer">Yes<i class="tick-box"></i></span><span class="answer">No<i class="tick-box"></i></span></div>
      <div class="item"><span class="item-name">Blood clots</span><span class="answer">Yes<i class="tick-box"></i></span><span class="answer">No<i class="tick-box"></i></span></div>
      <div class="item"><span class="item-name">Leukemia</span><span class="answer">Yes<i class="tick-box"></i></span><span class="answer">No<i class="tick-box"></i></span></div>
      <div class="item"><span class="item-name">Low platelets</span><span class="answer">Yes<i class="tick-box"></i></span><span class="answer">No<i class="tick-box"></i></span></div>
      <div class="item"><span class="item-name">Lymphoma</span><span class="answer">Yes<i class="tick-box"></i></span><span class="answer">No<i class="tick-box"></i></span></div>
      <div class="item"><span class="item-name">Haemophelia</span><span class="answer">Yes<i class="tick-box"></i></span><span class="answer">No<i class="tick-box"></i></span></div>
      <div class="section-title">Chest</div>
      <div class="item"><span class="item-name">Bronchitis</span><span class="answer">Yes<i class="tick-box"></i></span><span class="answer">No<i class="tick-box"></i></span></div>
      <div class="item"><span class="item-name">Cystic Fibrosis</span><span class="answer">Yes<i class="tick-box"></i></span><span class="answer">No<i class="tick-box"></i></span></div>
      <div class="item"><span class="item-name">Emphysema</span><span class="answer">Yes<i class="tick-box"></i></span><span class="answer">No<i class="tick-box"></i></span></div>
      <div class="item"><span class="item-name">Pneumonia</span><span class="answer">Yes<i class="tick-box"></i></span><span class="answer">No<i class="tick-box"></i></span></div>
      <div class="section-title">Infectious Disease</div>
      <div class="item"><span class="item-name">Creutzfeldt-Jakob Disease</span><span class="answer">Yes<i class="tick-box"></i></span><span class="answer">No<i class="tick-box"></i></span></div>
      <div class="item"><span class="item-name">Hepatitis A,B,C,D</span><span class="answer">Yes<i class="tick-box"></i></span><span class="answer">No<i class="tick-box"></i></span></div>
    </div>

    <div class="history-col">
      <div class="item"><span class="item-name">HIV/AIDS</span><span class="answer">Yes<i class="tick-box"></i></span><span class="answer">No<i class="tick-box"></i></span></div>
      <div class="item"><span class="item-name">Influenza</span><span class="answer">Yes<i class="tick-box"></i></span><span class="answer">No<i class="tick-box"></i></span></div>
      <div class="item"><span class="item-name">Shingles</span><span class="answer">Yes<i class="tick-box"></i></span><span class="answer">No<i class="tick-box"></i></span></div>
      <div class="item"><span class="item-name">Tuberculosis</span><span class="answer">Yes<i class="tick-box"></i></span><span class="answer">No<i class="tick-box"></i></span></div>
      <div class="section-title">Heart</div>
      <div class="item"><span class="item-name">Angina</span><span class="answer">Yes<i class="tick-box"></i></span><span class="answer">No<i class="tick-box"></i></span></div>
      <div class="item"><span class="item-name">Atrial Fibrillation</span><span class="answer">Yes<i class="tick-box"></i></span><span class="answer">No<i class="tick-box"></i></span></div>
      <div class="item"><span class="item-name">Blood Pressure (High/Low)</span><span class="answer">Yes<i class="tick-box"></i></span><span class="answer">No<i class="tick-box"></i></span></div>
      <div class="item"><span class="item-name">Congenital Heart Disease</span><span class="answer">Yes<i class="tick-box"></i></span><span class="answer">No<i class="tick-box"></i></span></div>
      <div class="item"><span class="item-name">Heart attack</span><span class="answer">Yes<i class="tick-box"></i></span><span class="answer">No<i class="tick-box"></i></span></div>
      <div class="item"><span class="item-name">Heart murmur</span><span class="answer">Yes<i class="tick-box"></i></span><span class="answer">No<i class="tick-box"></i></span></div>
      <div class="item"><span class="item-name">Heart surgery</span><span class="answer">Yes<i class="tick-box"></i></span><span class="answer">No<i class="tick-box"></i></span></div>
      <div class="item"><span class="item-name">Heart valve replacement</span><span class="answer">Yes<i class="tick-box"></i></span><span class="answer">No<i class="tick-box"></i></span></div>
      <div class="item"><span class="item-name">Infective endocarditis</span><span class="answer">Yes<i class="tick-box"></i></span><span class="answer">No<i class="tick-box"></i></span></div>
      <div class="item"><span class="item-name">Rheumatic Heart Disease</span><span class="answer">Yes<i class="tick-box"></i></span><span class="answer">No<i class="tick-box"></i></span></div>
      <div class="item"><span class="item-name">Pacemaker</span><span class="answer">Yes<i class="tick-box"></i></span><span class="answer">No<i class="tick-box"></i></span></div>
      <div class="item"><span class="item-name">Stent</span><span class="answer">Yes<i class="tick-box"></i></span><span class="answer">No<i class="tick-box"></i></span></div>
      <div class="section-title">Other</div>
      <div class="item"><span class="item-name">Anxiety/PTSD</span><span class="answer">Yes<i class="tick-box"></i></span><span class="answer">No<i class="tick-box"></i></span></div>
      <div class="item"><span class="item-name">Arthritis</span><span class="answer">Yes<i class="tick-box"></i></span><span class="answer">No<i class="tick-box"></i></span></div>
      <div class="item"><span class="item-name">Alzheimer’s</span><span class="answer">Yes<i class="tick-box"></i></span><span class="answer">No<i class="tick-box"></i></span></div>
      <div class="item"><span class="item-name">Asthma</span><span class="answer">Yes<i class="tick-box"></i></span><span class="answer">No<i class="tick-box"></i></span></div>
      <div class="item"><span class="item-name">Anaphylaxis</span><span class="answer">Yes<i class="tick-box"></i></span><span class="answer">No<i class="tick-box"></i></span></div>
      <div class="item"><span class="item-name">Auto-immune disease</span><span class="answer">Yes<i class="tick-box"></i></span><span class="answer">No<i class="tick-box"></i></span></div>
      <div class="item"><span class="item-name">Coeliac</span><span class="answer">Yes<i class="tick-box"></i></span><span class="answer">No<i class="tick-box"></i></span></div>
      <div class="item"><span class="item-name">Depression</span><span class="answer">Yes<i class="tick-box"></i></span><span class="answer">No<i class="tick-box"></i></span></div>
      <div class="item"><span class="item-name">Diabetes</span><span class="answer">Yes<i class="tick-box"></i></span><span class="answer">No<i class="tick-box"></i></span></div>
      <div class="item"><span class="item-name">Epilepsy</span><span class="answer">Yes<i class="tick-box"></i></span><span class="answer">No<i class="tick-box"></i></span></div>
      <div class="item"><span class="item-name">Kidney Disease</span><span class="answer">Yes<i class="tick-box"></i></span><span class="answer">No<i class="tick-box"></i></span></div>
      <div class="item"><span class="item-name">Liver Disease</span><span class="answer">Yes<i class="tick-box"></i></span><span class="answer">No<i class="tick-box"></i></span></div>
      <div class="item"><span class="item-name">Osteoporosis</span><span class="answer">Yes<i class="tick-box"></i></span><span class="answer">No<i class="tick-box"></i></span></div>
      <div class="item"><span class="item-name">Parkinson’s</span><span class="answer">Yes<i class="tick-box"></i></span><span class="answer">No<i class="tick-box"></i></span></div>
      <div class="item"><span class="item-name">Radiation to Head/Neck</span><span class="answer">Yes<i class="tick-box"></i></span><span class="answer">No<i class="tick-box"></i></span></div>
      <div class="item"><span class="item-name">Schizophrenia</span><span class="answer">Yes<i class="tick-box"></i></span><span class="answer">No<i class="tick-box"></i></span></div>
      <div class="item"><span class="item-name">Snoring</span><span class="answer">Yes<i class="tick-box"></i></span><span class="answer">No<i class="tick-box"></i></span></div>
      <div class="item"><span class="item-name">Sleep apnea</span><span class="answer">Yes<i class="tick-box"></i></span><span class="answer">No<i class="tick-box"></i></span></div>
      <div class="item"><span class="item-name">Stroke</span><span class="answer">Yes<i class="tick-box"></i></span><span class="answer">No<i class="tick-box"></i></span></div>
    </div>
  </section>

  <footer class="sign-off">
    <div class="sign-lines">
      <div class="sign-field date"><span class="sign-label">Date</span><span class="sign-rule"></span></div>
      <div class="sign-field"><span class="sign-label">Signature</span><span class="sign-rule"></span></div>
    </div>
    <p class="thanks">Thank you for the time to complete your medical history form.<br>Oral health is linked to overall health and this comprehensive questionnaire will help us to provide you with optimal and safe care.</p>
  </footer>
  <div class="footer-tab"></div>
  <div class="footer-band"></div>
</main>
</body>
</html>
```